Open Horizon Project

I am creating a personal blog to outline, in pictures and words, the cultural decay of everyday life in Australia today. This has been manifested by the rise of a nanny state.
Australia's foundation was based on hardened men i.e.- convicts, lifeguards, determined, strong men. Today Australia has become a Nanny State where everything is banned e.g.- it's illegal not to wear a helmet on a bike; it's illegal to chop down or prune trees on your own property. It's now a place where a city parking space might have 7-10 signs outlining a different set of parking laws for different timezones and days of the week. I could type forever.
Obviously I am looking for a neat wordpress designed blog with a focus on having a great banner that gives an indication of this change. From strong, determined individuals to a nation being forced to cower under a nanny. I'm open to your interpretation.
The blog title is "Open Horizon" with a byline of "what the bloody hell happened".

```html
<!DOCTYPE html>
<html lang="en">
<head>
<meta charset="utf-8">
<title>Open Horizon</title>
<link rel="stylesheet" href="https://fonts.googleapis.com/css2?family=Oswald:wght@400;500;600;700&family=Open+Sans:wght@400;600;700&display=swap">
<style>
:root{
  --red:#d8231f;
  --ink:#222222;
  --dark:#262626;
  --text:#555555;
  --muted:#777777;
  --page:#f0f0f0;
  --white:#ffffff;
  --line:#dddddd;
  --gold:#f2a51c;
  --footer:#1e1e1e;
}
*{margin:0;padding:0;box-sizing:border-box}
html,body{width:1200px;height:2510px;overflow:hidden}
body{background:var(--page);font-family:"Open Sans",Arial,sans-serif;color:var(--text);position:relative}
.abs{position:absolute}

/* header */
.site-header{left:0;top:0;width:1200px;height:80px;background:var(--white)}
.brand{left:132px;top:18px;display:flex;align-items:center;gap:12px}
.brand-mark{width:30px;height:30px;border-radius:50%;background:var(--gold)}
.brand-name{font-family:"Oswald",sans-serif;font-weight:700;font-size:32px;color:var(--red);letter-spacing:.5px;line-height:1;white-space:nowrap}
.main-nav{top:29px;left:698px;font-family:"Oswald",sans-serif;font-size:14px;color:var(--ink);text-transform:uppercase}
.main-nav span{position:absolute;white-space:nowrap}
.main-nav .active{color:var(--red)}
.search{left:1052px;top:31px}

/* hero */
.hero{left:0;top:80px;width:1200px;height:534px;background:
  linear-gradient(180deg,rgba(0,0,0,0) 55%,rgba(0,0,0,.35) 100%),
  linear-gradient(90deg,#7d8a95 0%,#5c6a72 25%,#2f3a45 50%,#101822 75%,#0c1118 100%)}
.hero-caption{left:306px;top:532px;height:55px;display:flex}
.hero-arrow{width:54px;height:55px;background:#1c1c1c;display:flex;align-items:center;justify-content:center}
.hero-title{width:478px;height:55px;background:var(--gold);font-family:"Oswald",sans-serif;font-weight:600;font-size:31px;line-height:1;color:#1d1d1d;text-transform:uppercase;display:flex;align-items:center;justify-content:center;white-space:nowrap;letter-spacing:0}

/* section headers */
.section-head{height:47px;background:var(--dark);color:var(--white);font-family:"Oswald",sans-serif;font-weight:600;font-size:21px;text-transform:uppercase;padding-left:15px;display:flex;align-items:center;justify-content:space-between;padding-right:14px;white-space:nowrap}

/* posts */
.post-card{left:132px;width:671px;height:270px;background:var(--white);border:1px solid var(--line)}
.post-thumb{left:14px;top:14px;width:240px;height:240px}
.post-body{left:270px;top:16px;width:388px;height:240px}
.post-title{font-family:"Oswald",sans-serif;font-weight:400;font-size:17px;line-height:23px;color:var(--ink)}
.post-meta{display:flex;font-size:10.5px;color:var(--muted);margin-top:12px;white-space:nowrap}
.post-meta span{display:inline-flex;align-items:center;gap:4px}
.post-meta span:nth-child(1){width:120px}
.post-meta span:nth-child(2){width:104px}
.post-excerpt{font-size:10.4px;line-height:17.4px;color:var(--text);margin-top:12px}
.read-more{position:absolute;left:0;top:195px;width:89px;height:34px;border:1px solid #cfcfcf;font-size:11px;color:var(--muted);display:flex;align-items:center;justify-content:center;background:var(--white)}

.pager{left:132px;top:2181px;display:flex;gap:10px}
.pager span{width:30px;height:30px;border-radius:50%;border:1px solid #cfcfcf;background:var(--white);font-size:12px;color:var(--muted);display:flex;align-items:center;justify-content:center}

/* sidebar */
.widget{left:828px;width:238px}
.widget-box{background:var(--white);border:1px solid var(--line);padding:17px 14px 0}
.side-item{display:flex;gap:10px;height:72px}
.side-thumb{width:57px;height:47px;flex:none}
.side-title{font-family:"Oswald",sans-serif;font-size:11.5px;line-height:15px;color:var(--ink)}
.side-date{font-size:8.5px;color:var(--muted);margin-top:4px;white-space:nowrap}
.video-thumb{width:208px;height:119px;position:relative;background:linear-gradient(180deg,#6a7b5f 0%,#8c5a3a 55%,#5a3a28 100%)}
.play{position:absolute;left:88px;top:43px;width:32px;height:32px;border-radius:50%;background:var(--white);display:flex;align-items:center;justify-content:center}
.video-title{font-family:"Oswald",sans-serif;font-size:11.5px;line-height:15px;color:var(--ink);margin-top:7px}

/* newsletter */
.newsletter{left:0;top:2294px;width:1200px;height:119px;background:var(--gold)}
.newsletter-label{left:335px;top:42px;font-family:"Open Sans",sans-serif;font-weight:700;font-size:28px;color:#1d1d1d;letter-spacing:1px;line-height:1;white-space:nowrap}
.newsletter-input{left:552px;top:42px;width:215px;height:36px;background:var(--white);font-size:12px;color:#333;padding-left:15px;display:flex;align-items:center}
.newsletter-btn{left:783px;top:42px;width:79px;height:36px;background:#1d1d1d;color:var(--white);font-family:"Oswald",sans-serif;font-weight:500;font-size:13px;display:flex;align-items:center;justify-content:center;text-transform:uppercase}

/* footer */
.site-footer{left:0;top:2413px;width:1200px;height:97px;background:var(--footer)}
.footer-links{left:132px;top:27px;font-size:11.5px;color:#cfcfcf;word-spacing:2px;white-space:nowrap}
.copyright{left:132px;top:54px;font-size:11px;color:#a9a9a9;white-space:nowrap}
.social{left:828px;top:34px;display:flex;gap:28px}
.social span{width:24px;height:24px;border-radius:50%;background:#8a8a8a}
</style>
</head>
<body>

<header class="site-header abs">
  <div class="brand abs"><span class="brand-mark"></span><span class="brand-name">OPEN HORIZON</span></div>
  <nav class="main-nav abs">
    <span class="active" style="left:0">Home</span>
    <span style="left:55px">About Us</span>
    <span style="left:134px">Gallery</span>
    <span style="left:203px">Videos</span>
    <span style="left:264px">Contact Us</span>
  </nav>
  <svg class="search abs" width="16" height="16" viewBox="0 0 16 16"><circle cx="6.5" cy="6.5" r="4.8" fill="none" stroke="#222" stroke-width="2"/><line x1="10" y1="10" x2="14.5" y2="14.5" stroke="#222" stroke-width="2.2"/></svg>
</header>

<section class="hero abs" role="img" aria-label="City skyline by day on the left blending into a night skyline with lit towers reflected in a river"></section>
<div class="hero-caption abs">
  <div class="hero-arrow"><svg width="14" height="20" viewBox="0 0 14 20"><path d="M11 2 3 10l8 8" fill="none" stroke="#fff" stroke-width="3"/></svg></div>
  <div class="hero-title">What the bloody hell happened</div>
  <div class="hero-arrow"><svg width="14" height="20" viewBox="0 0 14 20"><path d="M3 2l8 8-8 8" fill="none" stroke="#fff" stroke-width="3"/></svg></div>
</div>

<div class="section-head abs" style="left:132px;top:680px;width:671px">Recent Post</div>

<article class="post-card abs" style="top:736px">
  <div class="post-thumb abs" role="img" aria-label="Aboriginal rock art painted in white and red ochre" style="background:linear-gradient(135deg,#8a6048,#b88a70 50%,#6e4a38)"></div>
  <div class="post-body abs">
    <h2 class="post-title">Maecenas consequat justo enim, ac mattis massa imperdiet quis. Sed augue orci, elementum in magna</h2>
    <div class="post-meta"><span>25 November, 2017</span><span>&#9638; 87 Comments</span><span>&#10148; 71 Shares</span></div>
    <p class="post-excerpt">Vestibulum condimentum, risus ut posuere cursus, velit justo accumsan sem, lobortis aliquet metus dui eu libero. Pellentesque a imperdiet dolor, et auctor est. Fusce sollicitudin lorem et luctus volutpat. Proin placerat dapibus gravida. In tristique tristique nulla eget hendrerit. Maecenas vel tortor accumsan quam varius imperdiet vel eget elit. Aenean facilisis tincidunt lectus.</p>
    <span class="read-more">Read more</span>
  </div>
</article>

<article class="post-card abs" style="top:1024px">
  <div class="post-thumb abs" role="img" aria-label="Limestone sea stacks on a coast at sunset" style="background:linear-gradient(180deg,#4d7fb8 0%,#d9903e 45%,#b2521e 70%,#2d5a78 100%)"></div>
  <div class="post-body abs">
    <h2 class="post-title">Etiam mattis augue vehicula odio posuere, sit amet tempus lectus luctus</h2>
    <div class="post-meta"><span>25 November, 2017</span><span>&#9638; 87 Comments</span><span>&#10148; 71 Shares</span></div>
    <p class="post-excerpt">Vestibulum condimentum, risus ut posuere cursus, velit justo accumsan sem, lobortis aliquet metus dui eu libero. Pellentesque a imperdiet dolor, et auctor est. Fusce sollicitudin lorem et luctus volutpat. Proin placerat dapibus gravida. In tristique tristique nulla eget hendrerit. Maecenas vel tortor accumsan quam varius imperdiet vel eget elit. Aenean facilisis tincidunt lectus.</p>
    <span class="read-more">Read more</span>
  </div>
</article>

<article class="post-card abs" style="top:1312px">
  <div class="post-thumb abs" role="img" aria-label="Two koalas resting in a eucalyptus tree against blue sky" style="background:linear-gradient(160deg,#3f7fc8 0%,#7f9a78 45%,#8a8479 70%,#5d5a52 100%)"></div>
  <div class="post-body abs">
    <h2 class="post-title">Etiam vel massa elementum, bibendum tellus venenatis, feu-giat massa</h2>
    <div class="post-meta"><span>25 November, 2017</span><span>&#9638; 87 Comments</span><span>&#10148; 71 Shares</span></div>
    <p class="post-excerpt">Vestibulum condimentum, risus ut posuere cursus, velit justo accumsan sem, lobortis aliquet metus dui eu libero. Pellentesque a imperdiet dolor, et auctor est. Fusce sollicitudin lorem et luctus volutpat. Proin placerat dapibus gravida. In tristique tristique nulla eget hendrerit. Maecenas vel tortor accumsan quam varius imperdiet vel eget elit. Aenean facilisis tincidunt lectus.</p>
    <span class="read-more">Read more</span>
  </div>
</article>

<article class="post-card abs" style="top:1600px">
  <div class="post-thumb abs" role="img" aria-label="Red rock range above golden outback grassland under blue sky" style="background:linear-gradient(180deg,#2d5fa8 0%,#6f8fc0 30%,#a3462a 45%,#c9962e 65%,#8a6a22 100%)"></div>
  <div class="post-body abs">
    <h2 class="post-title">Aliquam erat volutpat. Quisque aliquet ex nec est vestibulum pulvinar. Pellentesque convallis molestie enim.</h2>
    <div class="post-meta"><span>25 November, 2017</span><span>&#9638; 87 Comments</span><span>&#10148; 71 Shares</span></div>
    <p class="post-excerpt">Vestibulum condimentum, risus ut posuere cursus, velit justo accumsan sem, lobortis aliquet metus dui eu libero. Pellentesque a imperdiet dolor, et auctor est. Fusce sollicitudin lorem et luctus volutpat. Proin placerat dapibus gravida. In tristique tristique nulla eget hendrerit. Maecenas vel tortor accumsan quam varius imperdiet vel eget elit. Aenean facilisis tincidunt lectus.</p>
    <span class="read-more">Read more</span>
  </div>
</article>

<article class="post-card abs" style="top:1888px">
  <div class="post-thumb abs" role="img" aria-label="Kangaroo silhouette against an orange sunset" style="background:linear-gradient(180deg,#4a3a2a 0%,#c97a20 35%,#f0a030 60%,#5a3010 100%)"></div>
  <div class="post-body abs">
    <h2 class="post-title">Vivamus lacus justo, ultrices nec erat in, euismod iaculis mauris. Vivamus eleifend vitae nulla vel malesuada.</h2>
    <div class="post-meta"><span>25 November, 2017</span><span>&#9638; 87 Comments</span><span>&#10148; 71 Shares</span></div>
    <p class="post-excerpt">Vestibulum condimentum, risus ut posuere cursus, velit justo accumsan sem, lobortis aliquet metus dui eu libero. Pellentesque a imperdiet dolor, et auctor est. Fusce sollicitudin lorem et luctus volutpat. Proin placerat dapibus gravida. In tristique tristique nulla eget hendrerit. Maecenas vel tortor accumsan quam varius imperdiet vel eget elit. Aenean facilisis tincidunt lectus.</p>
    <span class="read-more">Read more</span>
  </div>
</article>

<nav class="pager abs"><span>1</span><span>2</span><span>3</span><span>4</span><span>5</span><span>&lsaquo;</span><span>&rsaquo;</span></nav>

<aside class="widget abs" style="top:680px">
  <div class="section-head">Latest Post<svg width="12" height="18" viewBox="0 0 12 18"><path d="M2 2l7 7-7 7" fill="none" stroke="#fff" stroke-width="3"/></svg></div>
  <div class="widget-box" style="height:305px">
    <div class="side-item"><div class="side-thumb" role="img" aria-label="Coastal rock island" style="background:linear-gradient(180deg,#5c8fc4,#8a7a5c)"></div><div><div class="side-title">Suspendisse gravida ornare erat sed pulvainar.</div><div class="side-date">25 November, 2017</div></div></div>
    <div class="side-item"><div class="side-thumb" role="img" aria-label="Red monolith at dusk" style="background:linear-gradient(180deg,#3a6eb0,#c0582a)"></div><div><div class="side-title">Fusce nec leo ac urna pulvinar auctor. Mauris bibendum.</div><div class="side-date">25 November, 2017</div></div></div>
    <div class="side-item"><div class="side-thumb" role="img" aria-label="Harbour city skyline" style="background:linear-gradient(180deg,#8fb0d0,#5a6a5a)"></div><div><div class="side-title">Nulla in lorem at massa pellen-tesque posuere</div><div class="side-date">25 November, 2017</div></div></div>
    <div class="side-item"><div class="side-thumb" role="img" aria-label="Bridge over a harbour" style="background:linear-gradient(180deg,#9cc0e0,#3a6a90)"></div><div><div class="side-title">Nulla tristique posuere molestie. Aliquam erat volutpat</div><div class="side-date">25 November, 2017</div></div></div>
  </div>
</aside>

<aside class="widget abs" style="top:1048px">
  <div class="section-head">Popular Post<svg width="12" height="18" viewBox="0 0 12 18"><path d="M2 2l7 7-7 7" fill="none" stroke="#fff" stroke-width="3"/></svg></div>
  <div class="widget-box" style="height:302px">
    <div class="side-item"><div class="side-thumb" role="img" aria-label="Yellow road warning sign in the outback" style="background:linear-gradient(180deg,#d8a628,#7a5a2a)"></div><div><div class="side-title">Duis ornare erat eget magna dapibus, in accumsan</div><div class="side-date">25 November, 2017</div></div></div>
    <div class="side-item"><div class="side-thumb" role="img" aria-label="Rocky gorge at sunset" style="background:linear-gradient(180deg,#4a7ab0,#b0602a)"></div><div><div class="side-title">Nam tempus, quam in bibendum vulputate, sapien dolor viverra</div><div class="side-date">25 November, 2017</div></div></div>
    <div class="side-item"><div class="side-thumb" role="img" aria-label="Jetty at dusk" style="background:linear-gradient(180deg,#5a4a6a,#c09080)"></div><div><div class="side-title">Pellentesque blandit lacus eget nunc faucibus, et tincidunt</div><div class="side-date">25 November, 2017</div></div></div>
    <div class="side-item"><div class="side-thumb" role="img" aria-label="Turquoise coastline" style="background:linear-gradient(180deg,#6ab0c8,#2a7a7a)"></div><div><div class="side-title">Phasellus consequat sagittis nisi suscipit feugiat</div><div class="side-date">25 November, 2017</div></div></div>
  </div>
</aside>

<aside class="widget abs" style="top:1416px">
  <div class="section-head">Videos<svg width="12" height="18" viewBox="0 0 12 18"><path d="M2 2l7 7-7 7" fill="none" stroke="#fff" stroke-width="3"/></svg></div>
  <div class="widget-box" style="height:207px">
    <div class="video-thumb" role="img" aria-label="Aerial view of a red outback gorge with a waterfall">
      <span class="play"><svg width="12" height="14" viewBox="0 0 12 14"><path d="M2 1l9 6-9 6z" fill="#333"/></svg></span>
    </div>
    <div class="video-title">Cras eget leo sed nunc hendrerit ultricies eu at nisl iaculis faucibus urna</div>
    <div class="side-date">25 November, 2017</div>
  </div>
</aside>

<section class="newsletter abs">
  <div class="newsletter-label abs">NEWSLETTER</div>
  <div class="newsletter-input abs">Email Address</div>
  <div class="newsletter-btn abs">Subscribe</div>
</section>

<footer class="site-footer abs">
  <div class="footer-links abs">Home &nbsp;|&nbsp; About Us &nbsp;|&nbsp; Gallery &nbsp;|&nbsp; Videos &nbsp;|&nbsp; Contact Us</div>
  <div class="copyright abs">Copyright &copy; 2017 &nbsp;Open Horizon. &nbsp;All rights reserved.</div>
  <div class="social abs"><span></span><span></span><span></span><span></span><span></span></div>
</footer>

</body>
</html>
```